We require a post card design that is aimed at car dealerships. Our loan product enables them to sell more cards. Key messages you may want to consider are:

- Increased car sales for the dealer
- We service customers who can't obtain finance through main stream financial institutions

Contact details that must appear on the card

Dwayne Pellinger
dwayne@bluecovelending.com.au
0417 362 805

A space for an address label and postage stamp needs to be left.
Updates

Hi Guys,

Thank you for the designs you have posted so far. We are definitely on the right track.

The only thing I am looking for is making it a little more catchy in terms of word phrasing. We want a car dealership to look at the postcard and want to find out more about Blue Cove Lending.

" Do you want to see an increase in car sales"? < - Something along these lines.

You can also include a little more about Blue Cove Lending - Feel free to visit our website www.bluecovelending.com

Id also prefer not to have any pictures that include people, but I do love the car pictures that have been used so far.

If you have any questions please do not hesitate to ask.

Great job!!

Marguerite

Industry/Entity Type

Financial

```html
<!DOCTYPE html>
<html lang="en">
<head>
<meta charset="utf-8">
<title>Blue Cove Lending – Dealer Postcard</title>
<link href="https://fonts.googleapis.com/css2?family=Open+Sans:wght@400;800&family=Tinos:wght@400;700&display=swap" rel="stylesheet">
<style>
  :root{
    --page:#e9eae6;
    --green-deep:#1f2d22;
    --green-dark:#34463a;
    --green-mid:#5f7563;
    --green-soft:#a9b5a8;
    --address-light:#c9cec6;
    --address-dark:#8f988c;
    --accent:#3fae49;
    --ink-light:#f2f4f0;
    --ink-muted:#c4cdc3;
  }
  *{box-sizing:border-box;margin:0;padding:0}
  html,body{width:1200px;height:1000px;overflow:hidden;background:var(--page)}
  body{position:relative;font-family:"Open Sans",Arial,sans-serif}

  .postcard{position:absolute;left:160px;width:880px;height:460px;overflow:hidden;
    box-shadow:0 6px 18px rgba(0,0,0,.25)}
  .postcard--back{top:30px}
  .postcard--front{top:510px}

  /* back */
  .info-panel{position:absolute;left:0;top:0;width:500px;height:100%;
    background:linear-gradient(135deg,var(--green-mid) 0%,var(--green-dark) 45%,var(--green-deep) 100%);
    color:var(--ink-light);padding:34px 34px 0 36px;font-family:"Tinos","Times New Roman",serif}
  .info-intro{font-size:19px;font-weight:700;line-height:1.3;margin-bottom:14px}
  .info-lead{font-size:14px;font-weight:700;margin-bottom:10px}
  .product{font-size:10.5px;line-height:1.45;color:var(--ink-muted);margin-bottom:8px;font-family:"Open Sans",Arial,sans-serif}
  .product-name{color:var(--accent);font-family:"Tinos","Times New Roman",serif;font-weight:700;font-size:14px}
  .contact-strip{position:absolute;left:0;bottom:0;width:100%;height:118px;
    background:rgba(20,30,22,.55);padding:18px 36px;display:flex;justify-content:space-between;align-items:flex-end}
  .contact-name{font-size:19px;font-weight:700;margin-bottom:6px}
  .contact-line{display:flex;align-items:center;gap:8px;font-family:"Open Sans",Arial,sans-serif;font-size:11px;color:var(--ink-muted);margin-bottom:4px}
  .contact-line svg{width:12px;height:12px;fill:var(--ink-light)}
  .brand{display:flex;align-items:center;gap:8px;font-family:"Tinos","Times New Roman",serif;font-weight:700;font-size:14px;color:var(--ink-light)}
  .brand-square{width:16px;height:16px;background:var(--accent)}
  .address-area{position:absolute;left:500px;top:0;right:0;height:100%;
    background:linear-gradient(160deg,var(--address-light) 0%,#b4bbb1 50%,var(--address-dark) 100%)}

  /* front */
  .road-photo{position:absolute;inset:0;
    background:radial-gradient(ellipse at 78% 35%,#3a4a3d 0%,transparent 35%),
      linear-gradient(100deg,#d9ddd6 0%,#aab7a6 30%,#6f8a6c 55%,#4c6448 80%,#2f3d2f 100%)}
  .front-brand{position:absolute;left:36px;top:34px}
  .headline{position:absolute;left:36px;top:150px;font-weight:800;text-transform:uppercase;line-height:1}
  .headline-accent{display:block;color:var(--accent);font-size:64px;letter-spacing:1px}
  .headline-rest{display:block;color:var(--ink-light);font-size:40px;margin-top:6px}
  .tagline{position:absolute;left:36px;bottom:40px;color:var(--ink-light);font-size:15px;line-height:1.4;width:440px}
</style>
</head>
<body>

<section class="postcard postcard--back" aria-label="Postcard back">
  <div class="info-panel">
    <p class="info-intro">Blue Cove Lending sources highly competitive insurance products through Harbourline Insurance – our valued insurance partner.</p>
    <p class="info-lead">These products include:</p>
    <p class="product"><span class="product-name">GAP Insurance</span> – Gap cover with benefit subject to the policy limit. Pays the shortfall if a financed vehicle is written off and insurance falls short.</p>
    <p class="product"><span class="product-name">Comprehensive Insurance</span> – Covers the buyer's vehicle against accidental or malicious damage, fire, theft, storm and flood.</p>
    <p class="product"><span class="product-name">Consumer Credit Insurance</span> – Designed to help the buyer meet loan repayments if they are unable to work due to sickness, injury or involuntary unemployment.</p>
    <div class="contact-strip">
      <div class="contact">
        <p class="contact-name">Dwayne Pellinger</p>
        <p class="contact-line"><svg viewBox="0 0 12 12" aria-hidden="true"><path d="M0 2h12v8H0z M0 2l6 4 6-4" fill="none" stroke="#f2f4f0" stroke-width="1.2"/></svg>dwayne@bluecovelending.com.au</p>
        <p class="contact-line"><svg viewBox="0 0 12 12" aria-hidden="true"><path d="M2 0h3l1 3-2 1.5a7 7 0 0 0 3.5 3.5L9 6l3 1v3l-1.5 2C5 12 0 7 0 1.5z"/></svg>0417 362 805</p>
      </div>
      <div class="brand"><span class="brand-square"></span>Blue Cove Lending</div>
    </div>
  </div>
  <div class="address-area" aria-label="Space for address label and postage stamp"></div>
</section>

<section class="postcard postcard--front" aria-label="Postcard front">
  <div class="road-photo" role="img" aria-label="Photo of a green car's side mirror on a fast-moving road under a cloudy sky"></div>
  <div class="brand front-brand"><span class="brand-square"></span>Blue Cove Lending</div>
  <h1 class="headline">
    <span class="headline-accent">Increased</span>
    <span class="headline-rest">Car sales for<br>the dealer</span>
  </h1>
  <p class="tagline">We service customers who can't obtain finance through main stream financial institutions.</p>
</section>

</body>
</html>
```